Packaging redesign needed for recreational sport fishing products

We are looking for a cutting edge and modern/simplistic redesign to our current packaging for our line of recreational fishing products. Our current packaging is not uniform and we are looking for a template redesign that can be utilized amongst various types of packaging such as hang tags, header cards, and 4 sided boxed packages.

The fishing industry is a very conventional and traditional market where packaging is mundane and "old school". We are looking for something that will innovate and stand out from the traditional look and feel by incorporating digitized renditions of fish, crab, shrimp, and shellfish into the packaging of the intended targeted species for the product.

Size of Hang Cards ranges from:
2" x 4"
3" x 7"
8.5" x 11"

Header Cards range from:
6" x 4"
13" x 7"

Target Market(s)

Broad age, primarily male

Industry/Entity Type

Sporting Good

Font styles to use
Serif
Sans Serif

Colors
3176b5
000000
7f7f7f
aaaaaa
0255a3
fbed22
f37122
acd136

Requirements
Must have
• Bold, modern, simplistic, professional
Nice to have
• Large font easy to understand, fishing consumers vary in age from youth to the elder. Strong contrasting colors.
Should not have
• Pastels

```html
<!DOCTYPE html>
<html lang="en">
<head>
<meta charset="utf-8">
<title>Hang Tags – Crab Snare &amp; Lobster Divers Kit</title>
<link href="https://fonts.googleapis.com/css2?family=Nunito:wght@400;600;900&family=Varela+Round&display=swap" rel="stylesheet">
<style>
  :root {
    --sky-top: #2b55a4;
    --sky-bottom: #3fa9dc;
    --brand-blue: #0255a3;
    --lime: #acd136;
    --leaf: #4a9a36;
    --lobster-red: #d3302c;
    --orange: #f37122;
    --white: #ffffff;
    --crab-a: #8a5a2b;
    --crab-b: #4f3720;
    --shell-a: #e0492f;
    --shell-b: #a81f17;
  }
  * { margin: 0; padding: 0; box-sizing: border-box; }
  html, body { width: 1200px; height: 869px; overflow: hidden; background: var(--white); }
  body { position: relative; font-family: "Nunito", sans-serif; }

  .hang-tag { position: absolute; left: 96px; width: 1018px; overflow: hidden; background: var(--white); }
  .hang-tag--crab { top: 105px; height: 299px; }
  .hang-tag--lobster { top: 500px; height: 290px; }
  .tag-shapes { position: absolute; inset: 0; }

  .title { position: absolute; left: 200px; font-weight: 900; font-size: 74px; line-height: 1; letter-spacing: -3px; }
  .title-line { display: block; }
  .hang-tag--crab .title { top: 78px; }
  .hang-tag--crab .title-line--main { color: var(--leaf); }
  .hang-tag--crab .title-line--sub { color: var(--lime); margin-top: 2px; }
  .hang-tag--lobster .title { top: 72px; left: 198px; }
  .hang-tag--lobster .title-line--main { color: var(--lobster-red); }
  .hang-tag--lobster .title-line--sub { color: var(--orange); margin-top: 2px; margin-left: -2px; }

  .count-badge {
    position: absolute; left: 54px; top: 56px; width: 134px; height: 134px; border-radius: 50%;
    background: var(--lime); border: 6px solid var(--white);
    color: var(--white); font-weight: 900; font-size: 100px; line-height: 122px; text-align: center;
  }

  .features { position: absolute; display: flex; font-family: "Varela Round", sans-serif; font-size: 20px; letter-spacing: -0.4px; }
  .features li { list-style: none; padding: 0 8px; border-left: 1.5px solid currentColor; line-height: 32px; }
  .features li:first-child { border-left: none; padding-left: 0; }
  .hang-tag--crab .features { left: 86px; top: 251px; color: var(--leaf); }
  .hang-tag--lobster .features { left: 90px; top: 246px; color: var(--white); }

  .product-art { position: absolute; }
  .hang-tag--crab .product-art { left: 548px; top: 20px; width: 440px; height: 266px; }
  .hang-tag--lobster .product-art { left: 578px; top: 10px; width: 410px; height: 226px; }

  .brand-box {
    position: absolute; width: 176px; height: 86px; background: var(--white); border-radius: 6px;
    display: flex; align-items: center; justify-content: center; gap: 8px;
    font-family: "Nunito", sans-serif; font-weight: 900; font-size: 22px; letter-spacing: 3px; color: var(--brand-blue);
  }
  .brand-box .brand-dot { width: 16px; height: 16px; border-radius: 50%; background: var(--brand-blue); }
  .hang-tag--crab .brand-box { left: 790px; top: 200px; }
  .hang-tag--lobster .brand-box { left: 786px; top: 196px; }
</style>
</head>
<body>

<section class="hang-tag hang-tag--crab">
  <svg class="tag-shapes" viewBox="0 0 1018 299" width="1018" height="299" aria-hidden="true">
    <defs>
      <linearGradient id="sky-crab" x1="0" y1="0" x2="0" y2="1">
        <stop offset="0" stop-color="var(--sky-top)"/>
        <stop offset="0.6" stop-color="var(--sky-top)"/>
        <stop offset="1" stop-color="var(--sky-bottom)"/>
      </linearGradient>
    </defs>
    <path d="M0 0 H1018 V84 C860 74 720 58 560 66 C380 76 190 70 0 46 Z" fill="url(#sky-crab)"/>
    <path d="M0 104 C140 190 320 256 540 256 C720 256 860 222 1018 196 V299 H0 Z" fill="var(--lime)"/>
    <circle cx="512" cy="40" r="16" fill="var(--white)" stroke="#bdbdbd" stroke-width="2"/>
  </svg>

  <div class="count-badge">6</div>
  <h1 class="title">
    <span class="title-line title-line--main">Loop Crab</span>
    <span class="title-line title-line--sub">Snare</span>
  </h1>
  <ul class="features">
    <li>With Tangle Free Swivel</li>
    <li>Rust Resistant Coated Wire</li>
  </ul>

  <svg class="product-art" viewBox="0 0 440 266" role="img" aria-label="Photo of two brown crabs">
    <defs>
      <radialGradient id="crab-tone" cx="0.5" cy="0.5" r="0.6">
        <stop offset="0" stop-color="var(--crab-b)"/>
        <stop offset="1" stop-color="var(--crab-a)"/>
      </radialGradient>
    </defs>
    <ellipse cx="150" cy="140" rx="140" ry="120" fill="url(#crab-tone)"/>
    <ellipse cx="350" cy="95" rx="86" ry="78" fill="url(#crab-tone)"/>
  </svg>

  <div class="brand-box"><span class="brand-dot"></span>TIDEWELL</div>
</section>

<section class="hang-tag hang-tag--lobster">
  <svg class="tag-shapes" viewBox="0 0 1018 290" width="1018" height="290" aria-hidden="true">
    <defs>
      <linearGradient id="sky-lobster" x1="0" y1="0" x2="0" y2="1">
        <stop offset="0" stop-color="var(--sky-top)"/>
        <stop offset="0.6" stop-color="var(--sky-top)"/>
        <stop offset="1" stop-color="var(--sky-bottom)"/>
      </linearGradient>
    </defs>
    <path d="M0 0 H1018 V80 C860 64 720 40 560 44 C380 52 190 70 0 48 Z" fill="url(#sky-lobster)"/>
    <path d="M0 104 C150 200 340 244 560 244 C760 244 880 210 1018 200 V290 H0 Z" fill="var(--lobster-red)"/>
    <circle cx="511" cy="34" r="16" fill="var(--white)" stroke="#bdbdbd" stroke-width="2"/>
  </svg>

  <h2 class="title">
    <span class="title-line title-line--main">Lobster</span>
    <span class="title-line title-line--sub">Divers Kit</span>
  </h2>
  <ul class="features">
    <li>Mesh Catch Bag</li>
    <li>Lobster Gauge</li>
    <li>Grip Gloves</li>
    <li>Lobster Net</li>
  </ul>

  <svg class="product-art" viewBox="0 0 410 226" role="img" aria-label="Photo of a red lobster with raised claws">
    <defs>
      <radialGradient id="shell-tone" cx="0.5" cy="0.3" r="0.7">
        <stop offset="0" stop-color="var(--shell-b)"/>
        <stop offset="1" stop-color="var(--shell-a)"/>
      </radialGradient>
    </defs>
    <ellipse cx="205" cy="113" rx="200" ry="108" fill="url(#shell-tone)"/>
  </svg>

  <div class="brand-box"><span class="brand-dot"></span>TIDEWELL</div>
</section>

</body>
</html>
```